Nordavexa - world unique technology for better life - please let them know who am i at first sight

We need a new business card for company which is a provider of unique crystal based technology suitable for all living being. For more information and final design you can use our brochure (our colours are black and blue from brochure).
We use Verdana font

Industry/Entity Type

Business

Contact Information for Business Card

regular dimension

Other font styles liked:
• Verdana

Requirements
Must have
• Logo
• name
• function/position
• phone
• mobile
• e-mail
• adress
Nice to have
• inovative design (technology directed)

```html
<!DOCTYPE html>
<html lang="en">
<head>
<meta charset="utf-8">
<title>Nordavexa Business Card</title>
<link rel="stylesheet" href="https://fonts.googleapis.com/css2?family=Exo+2:wght@300;400;600&display=swap">
<style>
  :root {
    --page-bg: #e9ecef;
    --brand-blue: #07a3de;
    --brand-blue-deep: #0596cf;
    --swoosh-grey: #a7a9ac;
    --card-white: #ffffff;
    --card-grey: #e4e5e7;
    --ink: #2a2a2a;
    --on-blue: #ffffff;
  }
  * { margin: 0; padding: 0; box-sizing: border-box; }
  html, body {
    width: 1200px; height: 900px; overflow: hidden;
    background: var(--page-bg);
    font-family: "Exo 2", Verdana, sans-serif;
  }
  .business-card {
    position: absolute; left: 100px; top: 160px;
    width: 1000px; height: 580px;
    border-radius: 60px; overflow: hidden;
    box-shadow: 0 18px 40px rgba(0,0,0,0.18);
  }
  .card-background { position: absolute; inset: 0; }
  .brand {
    position: absolute; left: 44px; top: 92px;
    display: flex; align-items: center; gap: 22px;
  }
  .brand-mark {
    width: 104px; height: 104px; border-radius: 50%;
    background: var(--brand-blue);
  }
  .brand-name {
    font-weight: 300; font-size: 58px; letter-spacing: 2px;
    color: var(--brand-blue); text-transform: uppercase;
  }
  .person { position: absolute; left: 52px; top: 236px; }
  .person-name {
    font-weight: 600; font-size: 34px; letter-spacing: 2px;
    color: var(--brand-blue); text-transform: uppercase;
  }
  .person-role { font-weight: 400; font-size: 24px; color: var(--ink); margin-top: 2px; }
  .contact-list {
    position: absolute; left: 58px; top: 408px;
    list-style: none; color: var(--on-blue);
    font-size: 20px; letter-spacing: 1px;
  }
  .contact-item { display: flex; align-items: center; gap: 14px; height: 29px; }
  .contact-icon { width: 20px; height: 20px; fill: var(--on-blue); flex: none; }
  .address {
    position: absolute; right: 48px; top: 252px;
    text-align: right; color: var(--on-blue);
    font-size: 25px; line-height: 1.4; letter-spacing: 1px;
    font-style: normal;
  }
</style>
</head>
<body>
  <article class="business-card">
    <svg class="card-background" viewBox="0 0 1000 580" preserveAspectRatio="none" aria-hidden="true">
      <defs>
        <radialGradient id="paper-shade" cx="0.62" cy="0.45" r="0.7">
          <stop offset="0" stop-color="var(--card-white)"/>
          <stop offset="1" stop-color="var(--card-grey)"/>
        </radialGradient>
      </defs>
      <rect width="1000" height="580" fill="url(#paper-shade)"/>
      <path d="M0,392 C260,352 600,300 1000,128 L1000,580 L0,580 Z" fill="var(--brand-blue)"/>
      <path d="M0,376 C240,340 520,300 760,230 C620,285 330,345 0,392 Z" fill="var(--brand-blue-deep)"/>
      <path d="M420,338 C650,300 860,215 1000,98 L1000,132 C860,240 650,318 420,338 Z" fill="var(--swoosh-grey)"/>
    </svg>

    <div class="brand">
      <span class="brand-mark"></span>
      <span class="brand-name">Nordavexa</span>
    </div>

    <div class="person">
      <h1 class="person-name">Marek Halden</h1>
      <p class="person-role">Managing Director</p>
    </div>

    <ul class="contact-list">
      <li class="contact-item">
        <svg class="contact-icon" viewBox="0 0 24 24"><path d="M6.6 10.8a15 15 0 0 0 6.6 6.6l2.2-2.2c.3-.3.7-.4 1-.2 1.1.4 2.3.6 3.6.6.6 0 1 .4 1 1V20c0 .6-.4 1-1 1A17 17 0 0 1 3 4c0-.6.4-1 1-1h3.5c.6 0 1 .4 1 1 0 1.3.2 2.5.6 3.6.1.3 0 .7-.2 1z"/></svg>
        <span>014 552 7301</span>
      </li>
      <li class="contact-item">
        <svg class="contact-icon" viewBox="0 0 24 24"><path d="M7 1h10a2 2 0 0 1 2 2v18a2 2 0 0 1-2 2H7a2 2 0 0 1-2-2V3a2 2 0 0 1 2-2zm0 3v14h10V4zm5 15.5a1 1 0 1 0 0 2 1 1 0 0 0 0-2z"/></svg>
        <span>014 552 7302</span>
      </li>
      <li class="contact-item">
        <svg class="contact-icon" viewBox="0 0 24 24"><path d="M4 8h16v12H4zm3-6h10v5H7zm0 9v2h3v-2zm5 0v2h5v-2zm-5 4v2h3v-2zm5 0v2h5v-2z"/></svg>
        <span>014 552 7303</span>
      </li>
      <li class="contact-item">
        <svg class="contact-icon" viewBox="0 0 24 24"><path d="M2 5h20v14H2zm2 2v.5l8 5 8-5V7zm0 2.8V17h16V9.8l-8 5z"/></svg>
        <span>office@nordavexa.com</span>
      </li>
      <li class="contact-item">
        <svg class="contact-icon" viewBox="0 0 24 24"><path d="M12 2a10 10 0 1 0 0 20 10 10 0 0 0 0-20zm6.9 9h-3a15 15 0 0 0-1.3-5.6A8 8 0 0 1 18.9 11zM12 4.1c.9 1.2 1.8 3.6 1.9 6.9h-3.8c.1-3.3 1-5.7 1.9-6.9zM9.4 5.4A15 15 0 0 0 8.1 11h-3a8 8 0 0 1 4.3-5.6zM5.1 13h3a15 15 0 0 0 1.3 5.6A8 8 0 0 1 5.1 13zm6.9 6.9c-.9-1.2-1.8-3.6-1.9-6.9h3.8c-.1 3.3-1 5.7-1.9 6.9zm2.6-1.3a15 15 0 0 0 1.3-5.6h3a8 8 0 0 1-4.3 5.6z"/></svg>
        <span>www.nordavexa.com</span>
      </li>
    </ul>

    <address class="address">27 Harbour Lane, 5th floor<br>Kestrel Park KVR</address>
  </article>
</body>
</html>
```